Crimson Ledger.com is wanting to create a Facebook Ad to attract buyers to come to their website. We are wanting buyers to register for free and create an account on Crimson Ledger. com. We want to increase the number of buyers by posting an ad on Facebook groups. The buyer will click the link to our websites registration page.
https://www.crimsonledger.com/account/users/register

Semi Trucks
Semi Trailers
Construction Equipment
Farm Equipment
Trailers
ATV/UTV
Boats
RVs

```html
<!DOCTYPE html>
<html lang="en">
<head>
<meta charset="utf-8">
<title>Crimson Ledger – Heavy Truck Salvage Auction Site</title>
<link href="https://fonts.googleapis.com/css2?family=Montserrat:wght@800;900&family=Oswald:wght@500&family=Poppins:wght@400;600;700&display=swap" rel="stylesheet">
<style>
  :root {
    --orange: #e8652a;
    --black: #0d0d0d;
    --charcoal: #2e2e2e;
    --ink: #1e1e1e;
    --grey-text: #474747;
    --white: #ffffff;
    --stage: #c4c4c4;
    --machine-yellow: #f2b21c;
  }
  * { margin: 0; padding: 0; box-sizing: border-box; }
  html, body { width: 1200px; height: 923px; overflow: hidden; }
  body { background: var(--stage); position: relative; font-family: "Poppins", sans-serif; }

  .ad {
    position: absolute; left: 150px; top: 11px;
    width: 900px; height: 900px; overflow: hidden;
    background: var(--white);
  }
  .band-top {
    position: absolute; left: 0; top: 0; width: 900px; height: 345px;
    background: linear-gradient(100deg, #050505 0%, #111 45%, #2c2c2c 75%, #3a3a3a 100%);
  }
  .band-middle {
    position: absolute; left: 0; top: 345px; width: 900px; height: 418px;
    background: linear-gradient(90deg, #ffffff 0%, #f4f4f4 55%, #dedede 100%);
  }
  .band-bottom {
    position: absolute; left: 0; top: 762px; width: 900px; height: 138px;
    background: linear-gradient(180deg, #2a2a2a 0%, #333 50%, #262626 100%);
  }
  .torn-edge { position: absolute; left: 0; width: 900px; height: 14px; }
  .torn-edge--top { top: 338px; }
  .torn-edge--bottom { top: 755px; }

  .machine-photo { position: absolute; left: 440px; top: 255px; width: 460px; height: 505px; }

  .headline {
    position: absolute; left: 70px; top: 62px;
    font-family: "Montserrat", sans-serif; font-weight: 900;
    font-size: 78px; line-height: 79px; letter-spacing: -1px;
    color: var(--white); text-transform: uppercase;
  }

  .brand-name {
    position: absolute; left: 560px; top: 112px; width: 280px;
    font-family: "Montserrat", sans-serif; font-weight: 800;
    font-size: 46px; line-height: 50px; text-align: center;
    color: var(--white); text-transform: uppercase;
  }

  .site-tag {
    position: absolute; left: 0; top: 321px; width: 407px; height: 56px;
    background: var(--orange);
    box-shadow: 0 6px 8px rgba(0,0,0,.25);
    font-family: "Montserrat", sans-serif; font-weight: 800;
    font-size: 34px; letter-spacing: 6px; line-height: 56px;
    color: var(--white); padding-left: 66px;
  }

  .category-list {
    position: absolute; list-style: none;
    font-family: "Poppins", sans-serif; font-weight: 600;
    font-size: 23px; line-height: 36.5px; color: var(--ink);
  }
  .category-list--left { left: 64px; top: 403px; }
  .category-list--right { left: 324px; top: 403px; }
  .category-list li { position: relative; padding-left: 30px; }
  .category-list li.wrap { line-height: 24px; padding-top: 6px; }
  .tick { position: absolute; left: 0; top: 8px; width: 21px; height: 21px; }
  .category-list li.wrap .tick { top: 8px; }

  .register-badge { position: absolute; left: 64px; top: 600px; height: 54px; display: flex; align-items: stretch; }
  .register-badge__label {
    background: var(--black); color: var(--white);
    font-family: "Oswald", sans-serif; font-weight: 500;
    font-size: 36px; line-height: 54px; padding: 0 14px 0 16px;
    border-radius: 3px 0 0 3px; text-transform: uppercase; letter-spacing: -0.5px;
  }
  .register-badge__free {
    color: var(--orange);
    font-family: "Montserrat", sans-serif; font-weight: 900;
    font-size: 62px; line-height: 54px; padding-left: 3px; letter-spacing: -1px;
  }

  .account-prompt {
    position: absolute; left: 65px; top: 666px;
    font-size: 20px; font-weight: 400; color: var(--ink);
  }
  .account-site {
    position: absolute; left: 66px; top: 690px;
    display: flex; align-items: center; gap: 6px;
    font-size: 29px; font-weight: 700; color: var(--grey-text);
  }
  .account-site svg { width: 22px; height: 22px; }

  .link-note {
    position: absolute; left: 64px; top: 805px;
    font-size: 16px; line-height: 21px; font-weight: 600; color: var(--white);
  }
  .link-pill {
    position: absolute; left: 313px; top: 805px; width: 526px; height: 39px;
    background: var(--orange); border-radius: 10px;
    font-size: 15.5px; font-weight: 600; color: var(--white);
    line-height: 39px; text-align: center;
  }
</style>
</head>
<body>
  <main class="ad">
    <div class="band-top"></div>
    <div class="band-middle"></div>
    <div class="band-bottom"></div>

    <svg class="torn-edge torn-edge--top" viewBox="0 0 900 14" preserveAspectRatio="none" aria-hidden="true">
      <path d="M0 7 L40 4 L80 9 L130 5 L180 8 L240 3 L300 9 L360 5 L420 8 L480 4 L540 9 L600 5 L660 8 L720 4 L780 9 L840 5 L900 8 L900 14 L0 14 Z" fill="#fbfbfb"/>
    </svg>
    <svg class="torn-edge torn-edge--bottom" viewBox="0 0 900 14" preserveAspectRatio="none" aria-hidden="true">
      <path d="M0 0 L900 0 L900 6 L850 9 L790 4 L730 10 L670 5 L610 9 L550 4 L490 10 L430 5 L370 9 L310 4 L250 10 L190 5 L130 9 L70 4 L0 9 Z" fill="#f2f2f2"/>
    </svg>

    <svg class="machine-photo" role="img" aria-label="Photo of a yellow compact track loader framed by an orange gear shape" viewBox="0 0 460 505">
      <defs>
        <radialGradient id="machineTone" cx="0.62" cy="0.58" r="0.6">
          <stop offset="0" stop-color="var(--machine-yellow)"/>
          <stop offset="0.55" stop-color="#e9a11e"/>
          <stop offset="0.8" stop-color="#e8652a"/>
          <stop offset="1" stop-color="#d9561f"/>
        </radialGradient>
      </defs>
      <circle cx="320" cy="280" r="270" fill="url(#machineTone)"/>
    </svg>

    <h1 class="headline">Heavy<br>Truck<br>Salvage</h1>

    <div class="brand-name">Crimson Ledger</div>

    <div class="site-tag">AUCTION SITE</div>

    <ul class="category-list category-list--left">
      <li><svg class="tick" viewBox="0 0 20 20" aria-hidden="true"><circle cx="10" cy="10" r="10" fill="var(--orange)"/><path d="M5.5 10.3 L8.6 13.2 L14.5 7" fill="none" stroke="#fff" stroke-width="2.4" stroke-linecap="round" stroke-linejoin="round"/></svg>Semi Trucks</li>
      <li><svg class="tick" viewBox="0 0 20 20" aria-hidden="true"><circle cx="10" cy="10" r="10" fill="var(--orange)"/><path d="M5.5 10.3 L8.6 13.2 L14.5 7" fill="none" stroke="#fff" stroke-width="2.4" stroke-linecap="round" stroke-linejoin="round"/></svg>Semi Trailers</li>
      <li><svg class="tick" viewBox="0 0 20 20" aria-hidden="true"><circle cx="10" cy="10" r="10" fill="var(--orange)"/><path d="M5.5 10.3 L8.6 13.2 L14.5 7" fill="none" stroke="#fff" stroke-width="2.4" stroke-linecap="round" stroke-linejoin="round"/></svg>Farm Equipment</li>
      <li class="wrap"><svg class="tick" viewBox="0 0 20 20" aria-hidden="true"><circle cx="10" cy="10" r="10" fill="var(--orange)"/><path d="M5.5 10.3 L8.6 13.2 L14.5 7" fill="none" stroke="#fff" stroke-width="2.4" stroke-linecap="round" stroke-linejoin="round"/></svg>Construction<br>Equipment</li>
    </ul>

    <ul class="category-list category-list--right">
      <li><svg class="tick" viewBox="0 0 20 20" aria-hidden="true"><circle cx="10" cy="10" r="10" fill="var(--orange)"/><path d="M5.5 10.3 L8.6 13.2 L14.5 7" fill="none" stroke="#fff" stroke-width="2.4" stroke-linecap="round" stroke-linejoin="round"/></svg>Trailers</li>
      <li><svg class="tick" viewBox="0 0 20 20" aria-hidden="true"><circle cx="10" cy="10" r="10" fill="var(--orange)"/><path d="M5.5 10.3 L8.6 13.2 L14.5 7" fill="none" stroke="#fff" stroke-width="2.4" stroke-linecap="round" stroke-linejoin="round"/></svg>ATV/UTV</li>
      <li><svg class="tick" viewBox="0 0 20 20" aria-hidden="true"><circle cx="10" cy="10" r="10" fill="var(--orange)"/><path d="M5.5 10.3 L8.6 13.2 L14.5 7" fill="none" stroke="#fff" stroke-width="2.4" stroke-linecap="round" stroke-linejoin="round"/></svg>Boats</li>
      <li><svg class="tick" viewBox="0 0 20 20" aria-hidden="true"><circle cx="10" cy="10" r="10" fill="var(--orange)"/><path d="M5.5 10.3 L8.6 13.2 L14.5 7" fill="none" stroke="#fff" stroke-width="2.4" stroke-linecap="round" stroke-linejoin="round"/></svg>RVs</li>
    </ul>

    <div class="register-badge">
      <span class="register-badge__label">Register for</span>
      <span class="register-badge__free">FREE</span>
    </div>

    <p class="account-prompt">Create an account on</p>
    <p class="account-site">
      <svg viewBox="0 0 24 24" aria-hidden="true">
        <circle cx="12" cy="12" r="10" fill="none" stroke="var(--orange)" stroke-width="2.4"/>
        <ellipse cx="12" cy="12" rx="4.5" ry="10" fill="none" stroke="var(--orange)" stroke-width="2"/>
        <line x1="2" y1="12" x2="22" y2="12" stroke="var(--orange)" stroke-width="2"/>
      </svg>
      Crimson Ledger.com
    </p>

    <p class="link-note">Click the link to our<br>websites registration page</p>
    <div class="link-pill">https://www.crimsonledger.com/account/users/register</div>
  </main>
</body>
</html>
```